High End Notary Service Business Card Design

Want a professional and elegant/luxurious business card that is clean and simple in the design. A notary is a trusted professional that helps people sign very important documents. The card should be in alignment with this service provided.

Most of the time, service will be for the purchase of a home or refinance of a mortgage

There is NO LOGO. This is aesthetic. A look and feel. Conveying professionalism and concierge level of service.

Target Market(s)

Other business professionals, Lawyers, Escrow Officers, Loan Officers

Industry/Entity Type

Legal

Contact Information for Business Card

This will be a one-sided business card

Colors
35a7d7
3176b5
85cae6
d3a5cc
b868aa
ffffff
0356a4

Requirements
Must have
• Lorena T. Mirabel-Hodgkins
Notary Public

642-871-3094
MirabelSigningDesk@Wexmail.com
Nice to have
• Headshot photo below. Convey the aspect of signing documents. No black cards. Preference is shades of blue: light blue, navy, aqua, gold, white, or lavendar, etc.
Should not have
• No scales or legal scales.

```html
<!DOCTYPE html>
<html lang="en">
<head>
<meta charset="utf-8">
<title>Lorena T. Mirabel-Hodgkins — Notary Public Business Card</title>
<link href="https://fonts.googleapis.com/css2?family=Roboto:wght@400;500&display=swap" rel="stylesheet">
<style>
  :root {
    --page-bg: #e6e8eb;
    --card-white: #ffffff;
    --card-dark: #2b2c2d;
    --emboss-text: #262728;
    --accent-blue: #35a7d7;
    --body-grey: #6d6f72;
    --card-shadow: rgba(0, 0, 0, 0.22);
  }
  * { margin: 0; padding: 0; box-sizing: border-box; }
  html, body {
    width: 1200px;
    height: 900px;
    overflow: hidden;
    background: var(--page-bg);
    font-family: "Roboto", Arial, sans-serif;
  }
  .sheet {
    width: 1200px;
    height: 900px;
    display: flex;
    flex-direction: column;
    align-items: center;
    justify-content: center;
    gap: 50px;
  }
  .card {
    width: 630px;
    height: 360px;
    box-shadow: 0 10px 30px var(--card-shadow);
    display: flex;
    flex-direction: column;
    align-items: center;
    justify-content: center;
    text-align: center;
  }
  .card--front { background: var(--card-white); }
  .card--back {
    background: linear-gradient(160deg, #323334 0%, var(--card-dark) 55%, #242526 100%);
  }
  .card__name {
    font-weight: 500;
    font-size: 33px;
    letter-spacing: 0.2px;
    color: var(--accent-blue);
  }
  .card__title {
    margin-top: 4px;
    font-size: 15px;
    color: var(--body-grey);
  }
  .card__rule {
    width: 46px;
    height: 3px;
    margin: 16px 0 14px;
    background: var(--accent-blue);
  }
  .card__contact {
    font-size: 15px;
    line-height: 1.55;
    color: var(--body-grey);
  }
  .card__label {
    font-weight: 500;
    color: var(--accent-blue);
  }
  .card__name--emboss {
    font-size: 36px;
    color: var(--emboss-text);
    text-shadow:
      1px 1px 1px rgba(255, 255, 255, 0.16),
      -1px -1px 1px rgba(0, 0, 0, 0.55);
  }
</style>
</head>
<body>
  <main class="sheet">
    <section class="card card--front" aria-label="Card front">
      <h1 class="card__name">Lorena T. Mirabel-Hodgkins</h1>
      <p class="card__title">Notary Public</p>
      <div class="card__rule"></div>
      <p class="card__contact"><span class="card__label">P:</span> 642-871-3094</p>
      <p class="card__contact"><span class="card__label">E:</span> MirabelSigningDesk@Wexmail.com</p>
    </section>
    <section class="card card--back" aria-label="Card back">
      <p class="card__name card__name--emboss">Lorena T. Mirabel-Hodgkins</p>
    </section>
  </main>
</body>
</html>
```